Clearview Lung Institute of Houston Brochures

We need a redesign of our Brochures. We want to merge the two current brochure ideas into one cohesive, simple, and bold design. Notice that one design is generic and educational about Pulmonary Rehab in general. The other has our company branding and logo throughout. The front of the brochure needs to do better job of catching attention. We like the slogan: "Don't fight Shortness of Breathe Alone." The majority of our patients talk about how lonely the journey is dealing with chronic lung disease and shortness of breath. We have also updated our Logo since the last brochure design.
These brochures will be in Pulmonary Doctor waiting rooms and patient rooms.

Target Market(s)

Seniors 50+ with chronic lung disease in Houston Texas.

Industry/Entity Type

HealthCare

Colors
0054AA
0677BA
7BADD7
CADEEF
E8F1F8

Requirements
Must have
• Must have locations of 5 clinics. Must have visuals that aid in describing benefits of Pulmonary Rehab and Why pulmonary Rehab is right for them.
Nice to have
• Simple design. concise. Educational, yet not information overload.

```html
<!DOCTYPE html>
<html lang="en">
<head>
<meta charset="utf-8">
<title>Clearview Lung Institute of Houston – Brochure</title>
<link href="https://fonts.googleapis.com/css2?family=Raleway:wght@400;600&family=Roboto+Condensed:wght@400;700&family=Open+Sans:wght@400;600&family=Libre+Baskerville&display=swap" rel="stylesheet">
<style>
:root{
  --navy:#0b2566;
  --deep:#0a3a8c;
  --blue:#0054AA;
  --mid:#0677BA;
  --sky:#7BADD7;
  --pale:#CADEEF;
  --mist:#E8F1F8;
  --orange:#f07a1a;
  --slate:#2f4858;
  --teal:#1596c8;
  --grey:#9aa3ab;
  --green:#5aa832;
  --ink:#333a44;
  --bg:#e4e5e7;
}
*{box-sizing:border-box;margin:0;padding:0}
html,body{width:821px;height:1200px;overflow:hidden;background:var(--bg)}
body{position:relative;font-family:"Open Sans",sans-serif;color:var(--ink)}
.spread{position:absolute;left:80px;width:651px;height:501px;display:flex;box-shadow:0 10px 14px rgba(0,0,0,.18)}
.spread--outside{top:76px}
.spread--inside{top:622px}
.panel{position:relative;width:50%;height:100%;overflow:hidden}
.brand{font-family:"Raleway",sans-serif;font-weight:600;color:var(--blue);text-align:left;line-height:1.1;display:flex;align-items:center;gap:8px}
.brand__dot{width:22px;height:22px;border-radius:50%;background:var(--sky);flex:none}

/* back panel */
.back{background:linear-gradient(180deg,#fff,var(--mist))}
.back .brand{position:absolute;top:36px;left:72px;font-size:12px;letter-spacing:.5px}
.clinics{position:absolute;left:20px;right:10px;font-family:"Roboto Condensed",sans-serif;display:flex;gap:14px}
.clinics--row1{top:92px}
.clinics--row2{top:146px;left:76px}
.clinic{width:96px}
.clinic h3{font-weight:400;font-size:11.5px;color:var(--blue);margin-bottom:2px}
.clinic p{font-size:7.4px;line-height:1.2;color:var(--ink);display:flex;gap:3px}
.clinic svg{flex:none;margin-top:1px}
.map{position:absolute;left:40px;top:198px;width:300px;height:230px;border-radius:160px 0 0 0;background:radial-gradient(ellipse at 60% 55%,#fbf7e8,#eef2f4 70%);}
.back__band{position:absolute;left:0;bottom:0;width:100%;height:130px}
.back__info{position:absolute;left:0;bottom:14px;width:100%;text-align:center;color:#fff;font-family:"Roboto Condensed",sans-serif}
.back__info .name{font-size:11.5px;text-transform:uppercase;line-height:1.2}
.back__info p{font-size:11.5px;line-height:1.6}
.back__info .web{font-family:"Raleway",sans-serif;letter-spacing:2.6px;font-size:10.5px;margin-top:4px}

/* cover */
.cover{background:linear-gradient(180deg,#f6f8fb,#e3e9f1 45%)}
.cover .brand{position:absolute;top:46px;left:28px;font-size:16px;letter-spacing:.6px}
.cover__photo{position:absolute;left:20px;top:120px;width:306px;height:260px;border-radius:140px 0 0 0;background:radial-gradient(ellipse at 70% 40%,#f3dccb,#dfe6ee 60%,#e8edf3)}
.cover__band{position:absolute;left:0;bottom:0;width:100%;height:230px}
.cover__slogan{position:absolute;left:0;top:425px;width:100%;text-align:center;color:#fff;font-family:"Raleway",sans-serif;font-size:23px;line-height:1.3;letter-spacing:.3px}

/* inside left */
.why{background:#fff}
.why__head{position:absolute;inset:0 0 auto 0;height:190px;background:linear-gradient(160deg,var(--navy),var(--deep));}
.why__title{position:absolute;top:20px;width:100%;text-align:center;color:var(--sky);font-family:"Roboto Condensed",sans-serif;font-size:12px}
.why__intro{position:absolute;top:44px;left:20px;right:20px;text-align:center;color:#fff;font-family:"Roboto Condensed",sans-serif;font-size:9.4px;line-height:1.35}
.benefits{position:absolute;top:94px;left:10px;right:10px;display:flex;justify-content:space-between}
.benefit{width:74px;text-align:center;color:#fff;font-family:"Roboto Condensed",sans-serif;font-weight:700;font-size:5.6px;line-height:1.2}
.benefit svg{display:block;margin:0 auto 3px}
.why__pill{position:absolute;top:146px;left:0;width:182px;height:22px;background:linear-gradient(90deg,var(--sky),#a9cdea);border-radius:0 12px 12px 0;color:#fff;font-family:"Roboto Condensed",sans-serif;font-weight:700;font-size:11px;line-height:22px;padding-left:12px}
.reasons{position:absolute;top:180px;left:0;width:100%}
.reason{position:relative;height:79px;border-top:1px solid #e2e6ea}
.reason__label{position:absolute;left:18px;top:50%;transform:translateY(-50%);width:92px;font-family:"Libre Baskerville",serif;font-size:8.6px;line-height:1.3;color:#222}
.reason__shape{position:absolute;right:0;top:4px}
.reason__list{position:absolute;left:136px;right:8px;top:50%;transform:translateY(-50%);list-style:none;color:#fff;font-size:7.8px;line-height:1.3}
.reason__list li{margin:2px 0}
.reason__list--faint{color:#9ca4ab;font-size:7.2px}

/* inside right */
.cycle{background:linear-gradient(180deg,#eef3f9,#fff 60%)}
.cycle__pill{position:absolute;top:16px;left:63px;width:192px;height:22px;border-radius:11px;background:linear-gradient(90deg,var(--sky),#9cc6e8);color:#fff;text-align:center;font-family:"Roboto Condensed",sans-serif;font-weight:700;font-size:11px;line-height:22px}
.steps{position:absolute;top:50px;left:10px;width:306px}
.step{position:relative;height:54px;display:flex;align-items:center}
.step__photo{width:58px;height:44px;background:linear-gradient(135deg,#c9d3df,#9aa8b8);clip-path:polygon(20% 0,100% 0,100% 100%,20% 100%,0 50%)}
.step__note{width:86px;height:44px;display:flex;align-items:center;justify-content:center;text-align:center;color:#fff;font-size:7.6px;line-height:1.25;padding:0 4px}
.step__name{width:100px;height:54px;display:flex;align-items:center;padding-left:8px;color:#fff;font-family:"Roboto Condensed",sans-serif;font-size:11px;line-height:1.1}
.step__num{width:46px;height:46px;border-radius:50%;border:4px solid #fff;display:flex;align-items:center;justify-content:center;font-family:"Raleway",sans-serif;font-weight:600;font-size:26px;color:#fff;margin-left:-20px;box-shadow:0 0 0 2px rgba(0,0,0,.08)}
.cycle__text{position:absolute;top:300px;left:14px;right:14px;text-align:center;font-size:8.4px;line-height:1.4}
.cycle__text h2{font-family:"Roboto Condensed",sans-serif;font-size:11px;color:var(--blue);font-weight:700}
.cycle__cta{font-family:"Roboto Condensed",sans-serif;font-weight:700;color:var(--blue);font-size:11px;margin:12px 0 10px}
.cycle__small{font-size:7px;line-height:1.45}
.cycle__foot{margin-top:12px;font-family:"Roboto Condensed",sans-serif;font-weight:700;color:var(--blue);font-size:8.2px;line-height:1.3}
</style>
</head>
<body>

<section class="spread spread--outside">
  <div class="panel back">
    <div class="brand"><span class="brand__dot"></span><span>CLEARVIEW LUNG INSTITUTE<br>OF HOUSTON</span></div>

    <div class="clinics clinics--row1">
      <div class="clinic"><h3>Bellaire Clinic</h3>
        <p><svg width="6" height="6" viewBox="0 0 10 10"><path d="M2 1l2 2-1 1.5c.8 1.5 1.5 2.2 3 3L7.5 6l2 2-1.5 1.5C4 9 1 6 .5 2z" fill="#0054AA"/></svg>713-555-0199</p>
        <p><svg width="6" height="7" viewBox="0 0 10 12"><path d="M5 0a4 4 0 014 4c0 3-4 8-4 8S1 7 1 4a4 4 0 014-4z" fill="#0054AA"/></svg>4210 Maple Grove Ave Ste. A, Houston, TX 77081</p></div>
      <div class="clinic"><h3>Woodlands Clinic</h3>
        <p><svg width="6" height="6" viewBox="0 0 10 10"><path d="M2 1l2 2-1 1.5c.8 1.5 1.5 2.2 3 3L7.5 6l2 2-1.5 1.5C4 9 1 6 .5 2z" fill="#0054AA"/></svg>936-555-0127</p>
        <p><svg width="6" height="7" viewBox="0 0 10 12"><path d="M5 0a4 4 0 014 4c0 3-4 8-4 8S1 7 1 4a4 4 0 014-4z" fill="#0054AA"/></svg>2250 Pinecrest Dr #143, Shenandoah, TX 77385</p></div>
      <div class="clinic"><h3>Katy Freeway</h3>
        <p><svg width="6" height="6" viewBox="0 0 10 10"><path d="M2 1l2 2-1 1.5c.8 1.5 1.5 2.2 3 3L7.5 6l2 2-1.5 1.5C4 9 1 6 .5 2z" fill="#0054AA"/></svg>346-555-0163</p>
        <p><svg width="6" height="7" viewBox="0 0 10 12"><path d="M5 0a4 4 0 014 4c0 3-4 8-4 8S1 7 1 4a4 4 0 014-4z" fill="#0054AA"/></svg>1480 Willow Park Rd #800, Houston, TX 77077</p></div>
    </div>
    <div class="clinics clinics--row2">
      <div class="clinic"><h3>Clear Lake Clinic</h3>
        <p><svg width="6" height="6" viewBox="0 0 10 10"><path d="M2 1l2 2-1 1.5c.8 1.5 1.5 2.2 3 3L7.5 6l2 2-1.5 1.5C4 9 1 6 .5 2z" fill="#0054AA"/></svg>281-555-0148</p>
        <p><svg width="6" height="7" viewBox="0 0 10 12"><path d="M5 0a4 4 0 014 4c0 3-4 8-4 8S1 7 1 4a4 4 0 014-4z" fill="#0054AA"/></svg>905 Harbor View Rd Ste. A, Webster, TX 77598</p></div>
      <div class="clinic"><h3>Sugar Land</h3>
        <p><svg width="6" height="6" viewBox="0 0 10 10"><path d="M2 1l2 2-1 1.5c.8 1.5 1.5 2.2 3 3L7.5 6l2 2-1.5 1.5C4 9 1 6 .5 2z" fill="#0054AA"/></svg>281-555-0186</p>
        <p><svg width="6" height="7" viewBox="0 0 10 12"><path d="M5 0a4 4 0 014 4c0 3-4 8-4 8S1 7 1 4a4 4 0 014-4z" fill="#0054AA"/></svg>3320 Lakeside Ct #110, Sugar Land, TX 77479</p></div>
    </div>

    <div class="map" role="img" aria-label="Map of the Houston area with pins marking the five clinic locations"></div>

    <svg class="back__band" viewBox="0 0 326 130" preserveAspectRatio="none">
      <defs><linearGradient id="bandBack" x1="0" y1="0" x2="0" y2="1"><stop offset="0" stop-color="#0a3a8c"/><stop offset="1" stop-color="#0b2566"/></linearGradient></defs>
      <path d="M0 18 C80 38 160 38 230 20 S300 4 326 10 V130 H0Z" fill="url(#bandBack)"/>
    </svg>
    <div class="back__info">
      <div class="name">Clearview Lung Institute of Houston</div>
      <p>Pulmonary Therapy</p>
      <p>713 555 0199</p>
      <div class="web">www.clearviewlung.org</div>
    </div>
  </div>

  <div class="panel cover">
    <div class="brand"><span class="brand__dot"></span><span>CLEARVIEW LUNG INSTITUTE<br>OF HOUSTON</span></div>
    <div class="cover__photo" role="img" aria-label="Photo of a smiling senior couple with a friendly care team in the background"></div>
    <svg class="cover__band" viewBox="0 0 326 230" preserveAspectRatio="none">
      <defs>
        <linearGradient id="bandCover" x1="0" y1="0" x2="0" y2="1"><stop offset="0" stop-color="#0677BA"/><stop offset=".35" stop-color="#0a3a8c"/><stop offset="1" stop-color="#0b2566"/></linearGradient>
      </defs>
      <path d="M0 70 C70 30 160 30 230 50 S300 60 326 30 V230 H0Z" fill="#7BADD7" opacity=".6"/>
      <path d="M0 95 C80 55 170 55 240 70 S310 70 326 52 V230 H0Z" fill="url(#bandCover)"/>
    </svg>
    <div class="cover__slogan">Don't fight Shortness<br>of Breathe Alone</div>
  </div>
</section>

<section class="spread spread--inside">
  <div class="panel why">
    <div class="why__head"></div>
    <h2 class="why__title">A PATH TO BREATHING BETTER</h2>
    <p class="why__intro">People diagnosed with a chronic lung disease know that it is a serious and debilitating condition requiring ongoing medical attention. But many do not realize that pulmonary rehabilitation may help them live and breathe better.</p>
    <div class="benefits">
      <div class="benefit"><svg width="34" height="26" viewBox="0 0 34 26"><rect x="2" y="3" width="12" height="20" rx="1" fill="none" stroke="#8bc34a" stroke-width="1.6"/><rect x="20" y="3" width="12" height="20" rx="1" fill="none" stroke="#8bc34a" stroke-width="1.6"/><path d="M5 9h6M5 13h6M5 17h6M23 9h6M23 13h6M23 17h6" stroke="#fff" stroke-width="1.2"/></svg>Reduce Symptoms</div>
      <div class="benefit"><svg width="26" height="26" viewBox="0 0 26 26"><circle cx="13" cy="5" r="3" fill="#7BADD7"/><path d="M5 8l8 4 8-4M13 12v7l-4 6M13 19l4 6" stroke="#7BADD7" stroke-width="2.4" fill="none" stroke-linecap="round"/></svg>Increase Physical Activity</div>
      <div class="benefit"><svg width="26" height="26" viewBox="0 0 26 26"><rect x="3" y="4" width="20" height="19" rx="1.5" fill="none" stroke="#fff" stroke-width="1.4"/><path d="M3 9h20" stroke="#fff" stroke-width="1.4"/><path d="M7 13h3M12 13h3M17 13h3M7 17h3M12 17h3M17 17h3" stroke="#fff" stroke-width="1.6"/></svg>Improve Daily Life Function</div>
      <div class="benefit"><svg width="30" height="26" viewBox="0 0 30 26"><rect x="4" y="14" width="5" height="8" fill="#f07a1a"/><rect x="12" y="10" width="5" height="12" fill="#f07a1a"/><rect x="20" y="4" width="5" height="18" fill="#f07a1a"/><circle cx="14" cy="23" r="3" fill="#f5a623"/></svg>Improve Emotional Health</div>
    </div>
    <div class="why__pill">WHY PULMONARY THERAPY?</div>

    <div class="reasons">
      <div class="reason">
        <div class="reason__label">Shortness of Breath/ Trouble Breathing</div>
        <svg class="reason__shape" width="206" height="71" viewBox="0 0 206 71"><path d="M26 0H206V71H26L0 35Z" fill="var(--orange)"/></svg>
        <ul class="reason__list"><li>- Strengthen lungs and surrounding muscles</li><li>- Education on oxygen use</li><li>- Learn new breathing and oxygen conservation techniques</li></ul>
      </div>
      <div class="reason">
        <div class="reason__label">Fatigue/ Weakness</div>
        <svg class="reason__shape" width="206" height="71" viewBox="0 0 206 71"><path d="M26 0H206V71H26L0 35Z" fill="var(--slate)"/></svg>
        <ul class="reason__list"><li>- Increase stamina</li><li>- Strengthen key muscles</li><li>- Increase confidence</li><li>- Get back in shape in a controlled, safe, and supportive environment</li></ul>
      </div>
      <div class="reason">
        <div class="reason__label">Chronic Cough/ Illness</div>
        <svg class="reason__shape" width="206" height="71" viewBox="0 0 206 71"><path d="M26 0H206V71H26L0 35Z" fill="var(--teal)"/></svg>
        <ul class="reason__list"><li>- Strengthen Lungs</li><li>- Clear lungs using breathing tools and breathing techniques</li><li>- Build strength to fight future infections</li></ul>
      </div>
      <div class="reason">
        <div class="reason__label">Definition of Pulmonary Therapy</div>
        <svg class="reason__shape" width="206" height="71" viewBox="0 0 206 71"><defs><linearGradient id="fade" x1="0" x2="1"><stop offset="0" stop-color="#d4d9de"/><stop offset="1" stop-color="#f3f5f7"/></linearGradient></defs><path d="M26 0H206V71H26L0 35Z" fill="url(#fade)"/></svg>
        <p class="reason__list reason__list--faint">A program of education, exercise and training for those with chronic and severe lung disease. Consists of both 1 on 1 therapy and group therapy sessions, 2-3 times per week for 1 hour. Program ranges from 8-12 weeks depending on doctor recommendation.</p>
      </div>
    </div>
  </div>

  <div class="panel cycle">
    <div class="cycle__pill">BREAK THE CYCLE</div>
    <div class="steps">
      <div class="step"><div class="step__photo" role="img" aria-label="Photo of a man short of breath"></div><div class="step__note" style="background:var(--green)">Shortness of breath, coughing up mucus</div><div class="step__name" style="background:#4e9a2b">BREATHING DIFFICULTY</div><div class="step__num" style="background:var(--green)">1</div></div>
      <div class="step"><div class="step__photo" role="img" aria-label="Photo of a person resting at home"></div><div class="step__note" style="background:#3a3a3a">You cut back on activities</div><div class="step__name" style="background:#2a2a2a">INACTIVITY</div><div class="step__num" style="background:#2a2a2a">2</div></div>
      <div class="step"><div class="step__photo" role="img" aria-label="Photo of a tired senior woman"></div><div class="step__note" style="background:#a3a3a3">You become out of shape.</div><div class="step__name" style="background:#8c8c8c;font-size:9px">PHYSICAL DECONDITIONING</div><div class="step__num" style="background:#8c8c8c">3</div></div>
      <div class="step"><div class="step__photo" role="img" aria-label="Photo of a senior using a wheelchair"></div><div class="step__note" style="background:#4aa3e0">You can't do the simplest activities.</div><div class="step__name" style="background:#2b8fd6">DISABILITY</div><div class="step__num" style="background:#2b8fd6">4</div></div>
    </div>

    <div class="cycle__text">
      <h2>CLEARVIEW LUNG INSTITUTE OF HOUSTON</h2>
      <p>will help you break this cycle and give you the ability to overcome this progressive disease, regardless of the stage you are in. Beginning an exercise program is one of the most important steps in this process. Our team of healthcare professionals will guide you every step of the way as we tailor a program to fit your specific needs and goals.</p>
      <p class="cycle__cta">You CAN get your quality of life back!</p>
      <p class="cycle__small">Pulmonary Therapy services are covered under the majority of plans.<br>Clearview Lung Institute of Houston accepts Medicare and most private Insurance carriers.</p>
      <p class="cycle__small" style="margin-top:4px">For more information, including referral forms,<br>please visit www.clearviewlung.org or call (713) 555-0199.</p>
      <p class="cycle__foot">WWW.CLEARVIEWLUNG.ORG<br>© Clearview Lung Institute of Houston</p>
    </div>
  </div>
</section>

</body>
</html>
```